Album Jacket for young indie musicians in AFRICA #2 Baraka, Tumaini And Neema (Grace, Hope And Blessing)

We are ZEV SOUND (zev-sound.example), a music label for young African musicians living in a slum. I would like to ask you to design our new album's cover jacket. The title is Baraka, Tumaini And Neema (it means "Grace, Hope And Blessing" in Swahili. I entrust you whether you use English words in the design or not.), musician name is Jabari Okoth. Add our label logo (we have various versions and can provide). I attached Jabari Okoth's photo also. Please listen to the music of the album on Soundcloud. https://tunecove.example/tags/jabariokoth

Target Market(s)

International. not only African music funs.

Requirements
Must have
• Title, Musician's name, ZEV SOUND Logo
• In order to upload to iTunes, I require the final that the following conditions are met.
• 1400 x 1400 pixels
• JPG file type
• 72 - 300dpi (300dpi is the best)
• Less than 25mb
• RGB color scheme (not CMYK)
Nice to have
• His music is something bright and little funny. Please express the tone of music in the design.
Should not have
• African traditional image

```html
<!DOCTYPE html>
<html lang="en">
<head>
<meta charset="utf-8">
<title>Baraka, Tumaini &amp; Neema — Jabari Okoth</title>
<link rel="stylesheet" href="https://fonts.googleapis.com/css2?family=Montserrat:wght@300;400;800;900&display=swap">
<style>
  :root {
    --bg-deep: #240e10;
    --bg-warm: #7a3232;
    --bg-ember: #a04a3a;
    --magenta: #b0186e;
    --white: #ffffff;
    --soft-grey: #d9d6d6;
    --sun-yellow: #ffe500;
    --faint-grey: #6e6566;
    --rust: #6e2a1c;
    --olive: #5a4a1c;
    --ink: #111111;
    --photo-gold: #d8b93a;
    --photo-orange: #e88a1e;
  }
  html, body {
    margin: 0;
    padding: 0;
    width: 1200px;
    height: 1200px;
    overflow: hidden;
    background: var(--bg-deep);
  }
  .cover {
    position: relative;
    width: 1200px;
    height: 1200px;
    overflow: hidden;
    font-family: "Montserrat", sans-serif;
    background:
      radial-gradient(ellipse 700px 560px at 560px 560px, var(--bg-ember) 0%, var(--bg-warm) 35%, rgba(60,20,22,0.9) 70%, var(--bg-deep) 100%),
      var(--bg-deep);
  }
  .light-ray {
    position: absolute;
    left: 200px;
    top: 380px;
    width: 1000px;
    height: 6px;
    background: linear-gradient(90deg, transparent, rgba(255,190,150,0.35), transparent);
    transform: rotate(-18deg);
    filter: blur(3px);
  }
  .light-ray.second { top: 470px; left: 300px; transform: rotate(-8deg); opacity: 0.6; }
  .bokeh { position: absolute; inset: 0; }
  .glow {
    position: absolute;
    left: 230px;
    top: 250px;
    width: 820px;
    height: 950px;
    background:
      radial-gradient(ellipse 300px 520px at 50% 88%, #ffffff 0%, #ffffff 45%, rgba(255,240,235,0.75) 62%, rgba(255,200,190,0) 100%),
      radial-gradient(ellipse 380px 420px at 50% 30%, rgba(255,210,200,0.55) 0%, rgba(255,180,170,0) 100%);
  }
  .artist-photo {
    position: absolute;
    left: 420px;
    top: 330px;
    width: 450px;
    height: 570px;
    border-radius: 48% 48% 40% 40%;
    background:
      radial-gradient(ellipse at 45% 55%, var(--photo-orange) 0%, rgba(232,138,30,0.8) 30%, rgba(216,185,58,0.85) 55%, rgba(255,255,255,0) 78%);
  }
  .title {
    position: absolute;
    left: 60px;
    top: 40px;
    margin: 0;
    font-weight: 800;
    text-transform: uppercase;
    line-height: 1;
  }
  .title-line {
    display: block;
    font-size: 88px;
    letter-spacing: 1px;
    white-space: nowrap;
  }
  .title-baraka { color: var(--magenta); }
  .title-tumaini { color: var(--white); }
  .title-amp {
    position: absolute;
    left: 0;
    top: 140px;
    font-size: 78px;
    color: var(--soft-grey);
  }
  .title-neema {
    position: absolute;
    left: 0;
    top: 218px;
    width: 110px;
    text-align: center;
    font-size: 132px;
    line-height: 114px;
    color: var(--sun-yellow);
  }
  .title-neema span { display: block; }
  .translation {
    position: absolute;
    right: 50px;
    top: 230px;
    width: 190px;
    text-align: center;
    text-transform: uppercase;
  }
  .translation-grace {
    font-weight: 300;
    font-size: 62px;
    line-height: 68px;
    color: var(--faint-grey);
  }
  .translation-grace span, .translation-blessing span { display: block; }
  .translation-hope {
    margin-top: 34px;
    font-weight: 800;
    font-size: 56px;
    line-height: 60px;
    color: var(--rust);
  }
  .translation-blessing {
    margin-top: 24px;
    font-weight: 800;
    font-size: 42px;
    line-height: 41px;
    color: var(--olive);
  }
  .artist-name {
    position: absolute;
    left: 430px;
    top: 950px;
    width: 480px;
    text-align: center;
    color: var(--ink);
    text-transform: uppercase;
    margin: 0;
    line-height: 1;
  }
  .artist-first { display: block; font-weight: 300; font-size: 86px; }
  .artist-last { display: block; font-weight: 900; font-size: 98px; margin-top: 16px; }
  .label {
    position: absolute;
    left: 58px;
    top: 960px;
    display: flex;
    flex-direction: column;
    align-items: center;
    gap: 18px;
    width: 230px;
  }
  .label-mark {
    width: 110px;
    height: 110px;
    background: var(--white);
  }
  .label-name {
    font-weight: 800;
    font-size: 34px;
    color: var(--white);
    letter-spacing: 1px;
    white-space: nowrap;
  }
</style>
</head>
<body>
<main class="cover">
  <div class="light-ray"></div>
  <div class="light-ray second"></div>

  <svg class="bokeh" width="1200" height="1200" viewBox="0 0 1200 1200" aria-hidden="true">
    <circle cx="272" cy="885" r="80" fill="#ffffff" opacity="0.14"/>
    <circle cx="905" cy="335" r="14" fill="#ffffff" opacity="0.5"/>
    <circle cx="880" cy="410" r="52" fill="#ffffff" opacity="0.08"/>
    <circle cx="1140" cy="80" r="60" fill="#ffffff" opacity="0.05"/>
  </svg>

  <div class="glow"></div>
  <div class="artist-photo" role="img" aria-label="Photo of a smiling young man in a bright orange patterned shirt standing in front of a corrugated metal shack"></div>

  <h1 class="title">
    <span class="title-line"><span class="title-baraka">Baraka,</span> <span class="title-tumaini">Tumaini</span></span>
    <span class="title-amp">&amp;</span>
    <span class="title-neema"><span>N</span><span>E</span><span>E</span><span>M</span><span>A</span></span>
  </h1>

  <div class="translation">
    <div class="translation-grace"><span>G</span><span>R</span><span>A</span><span>C</span><span>E</span></div>
    <div class="translation-hope">Hope</div>
    <div class="translation-blessing"><span>&amp;</span><span>B</span><span>L</span><span>E</span><span>S</span><span>S</span><span>I</span><span>N</span><span>G</span></div>
  </div>

  <h2 class="artist-name">
    <span class="artist-first">Jabari</span>
    <span class="artist-last">Okoth</span>
  </h2>

  <div class="label">
    <div class="label-mark"></div>
    <div class="label-name">ZEV SOUND</div>
  </div>
</main>
</body>
</html>
```